TopQuizLane needs a dashboard page designed

Redesign the dashboard shown in the provided images.

There are two images:

NOTE: The vocabulary navigation on the left will be a very long list of words 100s, so keep that in mind when you're designing both the vocab navigation and the expanded vocab popup.

In the dashboard.png picture, there needs to be a progress chart showing the word progress like the following: review 1(show it as completed) -> review 2(show the user they are here) -> review 3(unvisited) -> review 4(unvisited)

The do-not-design-this-page.png image is for your reference only. It is not to be designed. Use it to understand the overall look and feel of the website to help you create the best dashboard page possible.
Updates

Need extra days to review

Industry/Entity Type

Education English learning

Number of Pages Required

1 page

Requirements
Must have
• The main navigation and main header cannot change between pages. See the do-not-design page for the main navigateion and header.
Should not have
• Do not add a person profile. We will not have images of our users. Keep the icons in the main navigation as they are.

```html
<!DOCTYPE html>
<html lang="en">
<head>
<meta charset="utf-8">
<title>TopQuizLane – Vocabulary Categories</title>
<link href="https://fonts.googleapis.com/css2?family=Roboto:wght@400;500;700&display=swap" rel="stylesheet">
<style>
  :root{
    --bar:#1b1e21;
    --rail:#24282c;
    --rail-active:#2e3236;
    --rail-text:#8a8f94;
    --page:#f4f4f4;
    --panel:#ffffff;
    --ink:#222222;
    --muted:#555a5f;
    --line:#e3e3e3;
    --chip:#f1f1f1;
    --accent:#c8102e;
    --accent-soft:#fde9ea;
    --ok:#2e9e5b;
    --star:#e6a817;
    --scrim:rgba(0,0,0,.72);
  }
  *{box-sizing:border-box;margin:0;padding:0}
  html,body{width:1200px;height:675px;overflow:hidden}
  body{font-family:"Roboto",sans-serif;background:var(--page);position:relative;color:var(--ink)}

  .top-bar{position:absolute;left:0;top:0;width:1200px;height:25px;background:var(--bar);display:flex;align-items:center;justify-content:center;color:#9aa0a6;font-size:11px}
  .top-bar .brand{display:flex;align-items:center;gap:4px}
  .top-bar .tools{position:absolute;right:10px;top:5px;display:flex;gap:14px}
  .top-bar .tools span{width:13px;height:13px;border-radius:50%;background:#7b8086;display:block}

  .side-rail{position:absolute;left:0;top:25px;width:52px;height:650px;background:var(--rail)}
  .rail-item{height:52px;display:flex;flex-direction:column;align-items:center;justify-content:center;gap:4px;color:var(--rail-text);font-size:6px}
  .rail-item.active{background:var(--rail-active)}
  .rail-item i{width:11px;height:11px;background:var(--rail-text);border-radius:2px;display:block}

  .vocab-panel{position:absolute;left:52px;top:25px;width:211px;height:650px;background:var(--panel);border-right:1px solid var(--line)}
  .vocab-panel .filter{margin:10px 18px;font-size:11px;color:var(--muted);display:flex;justify-content:space-between}
  .vocab-panel .expand{position:absolute;bottom:0;left:0;right:0;height:34px;border-top:1px solid var(--line);display:flex;align-items:center;justify-content:center;color:var(--accent);font-size:11px;gap:6px}

  .word-head{position:absolute;left:293px;top:42px;font-size:24px;font-weight:700}
  .steps{position:absolute;left:684px;top:52px;display:flex;gap:14px;font-size:10px}
  .steps .done{color:var(--ok)}
  .start-btn{position:absolute;left:1068px;top:43px;width:102px;height:30px;background:var(--accent);color:#fff;font-size:10px;display:flex;align-items:center;justify-content:center;border-radius:2px}

  .scrim{position:absolute;inset:0;background:var(--scrim)}

  .category-modal{position:absolute;left:60px;top:60px;width:1080px;height:555px;background:var(--panel);border-radius:4px;overflow:hidden}
  .modal-head{height:67px;background:#f7f7f7;border-bottom:1px solid var(--line);position:relative}
  .category-select{position:absolute;left:30px;top:18px;width:210px;height:30px;background:#fff;border:1px solid #cfcfcf;border-radius:3px;display:flex;align-items:center;justify-content:space-between;padding:0 9px;font-size:11px;color:var(--ink)}
  .close-btn{position:absolute;left:1037px;top:27px}

  .memory-group{position:absolute;left:30px}
  .group-title{display:flex;align-items:center;gap:9px;font-size:10.5px;font-weight:500;color:var(--ink)}
  .chips{display:flex;gap:4px;margin-top:11px}
  .chip{height:27px;padding:0 15px;border-radius:14px;background:var(--chip);font-size:10.5px;color:#333;display:flex;align-items:center;border:1px solid transparent}
  .chip.current{background:var(--accent-soft);border-color:var(--accent);color:var(--ink)}
</style>
</head>
<body>
  <header class="top-bar">
    <div class="brand">TopQuizLane
      <svg width="8" height="5" viewBox="0 0 8 5"><path d="M0 0h8L4 5z" fill="#9aa0a6"/></svg>
    </div>
    <div class="tools"><span></span><span></span><span></span></div>
  </header>

  <nav class="side-rail">
    <div class="rail-item active"><i></i>TopQuizLane</div>
    <div class="rail-item"><i></i>Daily English</div>
    <div class="rail-item"><i></i>Business</div>
  </nav>

  <aside class="vocab-panel">
    <div class="filter">All Categories <span>⌄</span></div>
    <div class="expand">⤢ Expand</div>
  </aside>

  <div class="word-head">Grab</div>
  <div class="steps">
    <span class="done">Review 1</span><span class="done">Review 2</span><span>Review 3</span><span>Review 4</span>
  </div>
  <div class="start-btn">Start Review</div>

  <div class="scrim"></div>

  <section class="category-modal">
    <div class="modal-head">
      <div class="category-select">All Categories
        <svg width="10" height="6" viewBox="0 0 10 6"><path d="M1 1l4 4 4-4" fill="none" stroke="#c8102e" stroke-width="1.4"/></svg>
      </div>
      <svg class="close-btn" width="12" height="12" viewBox="0 0 12 12"><path d="M1 1l10 10M11 1L1 11" stroke="#222" stroke-width="1.5"/></svg>
    </div>

    <div class="memory-group" style="top:98px">
      <div class="group-title">
        <svg width="12" height="12" viewBox="0 0 12 12"><circle cx="6" cy="7" r="4.3" fill="none" stroke="#222" stroke-width="1.3"/><path d="M4.5 1h3M6 7V4.5" stroke="#222" stroke-width="1.3"/></svg>
        Short-Term Memory
      </div>
      <div class="chips"><span class="chip current">Grab</span></div>
    </div>

    <div class="memory-group" style="top:182px">
      <div class="group-title">
        <svg width="12" height="12" viewBox="0 0 12 12"><rect x="2.5" y="2.5" width="7" height="7" rx="1" fill="none" stroke="#222" stroke-width="1.2"/><rect x="4.5" y="4.5" width="3" height="3" fill="none" stroke="#222"/><path d="M4 0.5v2M8 0.5v2M4 9.5v2M8 9.5v2M0.5 4h2M0.5 8h2M9.5 4h2M9.5 8h2" stroke="#222"/></svg>
        Working Memory
      </div>
      <div class="chips">
        <span class="chip">Cool Down</span><span class="chip">Crave</span><span class="chip">Go For</span><span class="chip">Go-To</span><span class="chip">In The Mood For</span><span class="chip">Grab</span><span class="chip">Sip</span><span class="chip">Soothing</span><span class="chip">Stick With</span><span class="chip">Throw In / Throw On</span>
      </div>
    </div>

    <div class="memory-group" style="top:266px">
      <div class="group-title">
        <svg width="12" height="12" viewBox="0 0 12 12"><rect x="2" y="5.5" width="8" height="6" rx="1" fill="none" stroke="#222" stroke-width="1.3"/><path d="M4 5.5V4a2 2 0 0 1 4 0v1.5" fill="none" stroke="#222" stroke-width="1.3"/></svg>
        Long-Term Memory
      </div>
      <div class="chips"><span class="chip">Give It A Try</span></div>
    </div>
  </section>
</body>
</html>
```